Stationery Design Project

Letterhead with logo and address
Envelopes with Logo and address

The target market is start-ups and
small to medium businesses primarly located in China, with less than 20
employees. Please have designers use Yellow and Blue colors and our logo
attached. Looking fr the same format as the business card attached.

Reason: Designer has been delayed working on web design

Target Market(s)

Start-ups and small to medium size businesses

Industry/Entity Type

Business

Font styles to use
Sans Serif

Requirements
Must have
• None
Nice to have
• None
Should not have
• N/A

```html
<!DOCTYPE html>
<html lang="en">
<head>
<meta charset="utf-8">
<title>Oktiva Letterhead</title>
<link rel="stylesheet" href="https://fonts.googleapis.com/css2?family=Montserrat:wght@400;500&display=swap">
<style>
  :root {
    --backdrop: #57504f;
    --paper: #efefee;
    --band-top: #0f5683;
    --band-bottom: #134b73;
    --brand-yellow: #f2c21b;
    --band-text: #c9d6e0;
    --address-text: #e6edf2;
  }
  * { margin: 0; padding: 0; box-sizing: border-box; }
  html, body {
    width: 1200px;
    height: 823px;
    overflow: hidden;
    background: var(--backdrop);
  }
  .canvas {
    position: relative;
    width: 1200px;
    height: 823px;
    display: flex;
    align-items: center;
    justify-content: center;
  }
  .letterhead {
    position: relative;
    width: 540px;
    height: 763px;
    background: var(--paper);
    display: flex;
    box-shadow: 0 18px 40px rgba(0, 0, 0, 0.28);
  }
  .side-band {
    width: 108px;
    height: 100%;
    background: linear-gradient(180deg, var(--band-top), var(--band-bottom));
    display: flex;
    flex-direction: column;
    align-items: center;
    justify-content: space-between;
    padding: 26px 10px 30px;
    font-family: "Montserrat", sans-serif;
  }
  .brand {
    display: flex;
    flex-direction: column;
    align-items: center;
    gap: 10px;
  }
  .brand-dot {
    width: 36px;
    height: 36px;
    border-radius: 50%;
    background: var(--brand-yellow);
  }
  .brand-name {
    font-size: 9px;
    font-weight: 500;
    letter-spacing: 3px;
    color: var(--band-text);
  }
  .address {
    align-self: flex-end;
    text-align: right;
    font-style: normal;
    font-size: 6.5px;
    line-height: 1.5;
    color: var(--address-text);
  }
  .address .contact-lines { margin-top: 4px; }
  .writing-area { flex: 1; }
</style>
</head>
<body>
  <main class="canvas">
    <article class="letterhead">
      <aside class="side-band">
        <div class="brand">
          <span class="brand-dot"></span>
          <span class="brand-name">OKTIVA</span>
        </div>
        <address class="address">
          <div>48 Cedar Row</div>
          <div>Millbrook</div>
          <div>New Hampshire</div>
          <div>United States</div>
          <div class="contact-lines">
            <div>P: 1 555-014-2280</div>
            <div>F: 1 555-014-2281</div>
          </div>
        </address>
      </aside>
      <section class="writing-area"></section>
    </article>
  </main>
</body>
</html>
```